Letterhead Design Project

Our firm recently came out with a new logo and new website and we would like to design letterhead that makes use of the new look.

Our firm is an energy consulting firm. We help our customers find ways to spend less money on their energy expenses (we cater to commercial and industrial accounts) by helping them find a lower rate for every unit of energy they consume, install more energy efficient measures so that they end up using fewer units of energy or determine if making the energy themselves can be done more cost effectively

Industry/Entity Type

Industrial

Requirements
Must have
• Must have our logo
must have our contact information
Nice to have
• some sort of watermark

```html
<!DOCTYPE html>
<html lang="en">
<head>
<meta charset="utf-8">
<title>Lumen Grid Partners Letterhead</title>
<link rel="stylesheet" href="https://fonts.googleapis.com/css2?family=Questrial&family=Source+Sans+3:wght@400&display=swap">
<style>
  :root {
    --paper: #ffffff;
    --ink: #4a4f55;
    --text: #222222;
    --accent: #5bbfcc;
    --accent-soft: #d6eef1;
  }
  * { margin: 0; padding: 0; box-sizing: border-box; }
  html, body { width: 900px; height: 1200px; overflow: hidden; background: var(--paper); }
  .letterhead {
    position: relative;
    width: 900px;
    height: 1200px;
    background: var(--paper);
    overflow: hidden;
  }
  .watermark-area {
    position: absolute;
    top: 0;
    right: 0;
    width: 380px;
    height: 620px;
    background: radial-gradient(ellipse at 75% 20%, var(--accent-soft) 0%, rgba(214,238,241,0.45) 45%, rgba(255,255,255,0) 75%);
  }
  .brand {
    position: absolute;
    top: 72px;
    left: 232px;
    display: flex;
    align-items: center;
    gap: 14px;
  }
  .brand-mark {
    width: 30px;
    height: 30px;
    background: var(--accent);
  }
  .brand-name {
    font-family: "Questrial", sans-serif;
    font-weight: 400;
    color: var(--ink);
    line-height: 1;
  }
  .brand-name .primary {
    display: block;
    font-size: 36px;
    letter-spacing: 9px;
  }
  .brand-name .secondary {
    display: block;
    font-size: 9px;
    letter-spacing: 14px;
    margin-top: 4px;
  }
  .footer {
    position: absolute;
    left: 0;
    right: 0;
    top: 1100px;
    text-align: center;
    font-family: "Source Sans 3", sans-serif;
    color: var(--text);
  }
  .footer-rule {
    width: 580px;
    height: 2px;
    margin: 0 auto 18px;
    background: linear-gradient(90deg, rgba(91,191,204,0), var(--accent) 50%, rgba(91,191,204,0));
  }
  .footer-address, .footer-contact {
    font-size: 15.5px;
    line-height: 24px;
  }
</style>
</head>
<body>
  <div class="letterhead">
    <div class="watermark-area" role="img" aria-label="Faint brand watermark decoration in pale teal"></div>

    <div class="brand">
      <span class="brand-mark"></span>
      <span class="brand-name">
        <span class="primary">LUMEN GRID</span>
        <span class="secondary">PARTNERS</span>
      </span>
    </div>

    <footer class="footer">
      <div class="footer-rule"></div>
      <p class="footer-address">Two Commerce Square, Suite 210 Riverton, NJ 07999</p>
      <p class="footer-contact">Phone : 201-555-0142 &nbsp;|&nbsp; Fax : 201-555-0178 | Email : info@lumengridpartners.com | www.LumenGridPartners.com</p>
    </footer>
  </div>
</body>
</html>
```